Menu Design Project

We are looking for a re-design of our menu.

We are an italian restaurant.

More info here:

http://www.tablereviewhub.com/Restaurant_Review-g71352-d836174-Reviews-Vellano-Rockland_Maine.html

website: vellanorestaurant.com

Restaurant

• Italian Design

Italian Colors

Easy to customize so we can add our own stuff quick

No need for heavy graphics or heavy colors

```html
<!DOCTYPE html>
<html lang="en">
<head>
<meta charset="utf-8">
<title>Vellano – Summer/Autumn Menu</title>
<link rel="stylesheet" href="https://fonts.googleapis.com/css2?family=Della+Respira&family=Cormorant+Garamond:ital,wght@0,500;0,700;1,500&display=swap">
<style>
  :root {
    --paper: #d6d0c6;
    --red: #a3161c;
    --band: #a80f16;
    --ink: #2e2a27;
    --logo: #4a4643;
    --rule: #8a8580;
    --bg: #ffffff;
    --display: "Della Respira", serif;
    --body: "Cormorant Garamond", serif;
  }
  * { box-sizing: border-box; margin: 0; padding: 0; }
  html, body { width: 1200px; height: 1200px; overflow: hidden; background: var(--bg); }
  .canvas { position: relative; width: 1200px; height: 1200px; overflow: hidden; }

  .sheet { position: absolute; background: var(--paper); border: 1px solid #b9b3aa; overflow: hidden; }
  .sheet-frame { position: absolute; inset: 12px; border: 1.5px solid var(--red); border-radius: 6px; }

  /* Cover */
  .cover { left: 24px; top: 12px; width: 476px; height: 1010px; }
  .cover .season { position: absolute; top: 72px; width: 100%; text-align: center; font: 14px var(--display), serif; color: var(--red); letter-spacing: 0.5px; }
  .wordmark { position: absolute; width: 100%; text-align: center; font-family: var(--display), serif; color: var(--logo); font-size: 36px; letter-spacing: 1px; }
  .cover .wordmark { top: 264px; }
  .cover .tagline { position: absolute; top: 402px; width: 100%; text-align: center; font: 30px var(--display), serif; color: var(--red); letter-spacing: 1px; }
  .cover .rule { position: absolute; left: 36px; right: 0; height: 1.5px; background: var(--red); }
  .cover .web { position: absolute; top: 660px; left: 78px; font: 22px var(--display), serif; color: var(--red); white-space: nowrap; }
  .cover .address { position: absolute; top: 738px; left: 0; width: 100%; text-align: center; font: 24px/31px var(--display), serif; color: var(--red); white-space: nowrap; }
  .cover .dots { position: absolute; left: 44px; right: 0; border-top: 4px dotted var(--red); }
  .cover .sourcing { position: absolute; top: 836px; left: 48px; font: 19px var(--display), serif; color: var(--red); white-space: nowrap; }
  .cover .daily { position: absolute; top: 896px; left: 72px; font: italic 18px/24px var(--display), serif; color: var(--red); white-space: nowrap; }

  /* Back */
  .back { left: 702px; top: 14px; width: 478px; height: 1012px; }
  .back .wordmark { top: 176px; }
  .back .motto { position: absolute; top: 262px; width: 100%; text-align: center; font: 17px var(--display), serif; color: var(--ink); }
  .back .heading { position: absolute; width: 100%; text-align: center; font: 36px var(--display), serif; color: var(--ink); }
  .hours { position: absolute; top: 424px; left: 124px; display: flex; gap: 38px; font: 10px/14px var(--body), serif; color: var(--ink); }
  .hours div { width: 70px; }
  .back .contact { position: absolute; top: 512px; width: 100%; text-align: center; font: 10px/11px var(--display), serif; color: var(--ink); }
  .back .phone { position: absolute; top: 566px; width: 100%; text-align: center; font: 10px var(--display), serif; color: var(--ink); }

  /* Inside menu */
  .menu { left: 312px; top: 457px; width: 572px; height: 607px; box-shadow: 0 0 3px rgba(0,0,0,0.25); }
  .menu-band { position: absolute; top: 27px; left: 0; right: 0; height: 40px; background: var(--band); }
  .menu-band::before, .menu-band::after { content: ""; position: absolute; left: 4px; right: 4px; border-top: 1px dashed rgba(255,255,255,0.75); }
  .menu-band::before { top: 3px; } .menu-band::after { bottom: 3px; }
  .menu-band span { position: absolute; top: 9px; font: 17px var(--display), serif; color: #fff; transform: translateX(-50%); white-space: nowrap; }

  .section { position: absolute; width: 234px; }
  .section h2 { font: 13px var(--display), serif; color: var(--red); font-weight: normal; padding-bottom: 3px; border-bottom: 1px solid var(--red); width: 108px; margin-bottom: 6px; white-space: nowrap; }
  .section .intro { font: 7px/9px var(--body), serif; color: var(--ink); margin-bottom: 4px; }
  .item { height: 21px; border-bottom: 1px dotted var(--rule); margin-bottom: 0; }
  .item-head { display: flex; justify-content: space-between; font: 700 8px/11px var(--body), serif; color: var(--red); font-variant: small-caps; }
  .item-head .price { font-weight: 500; }
  .item p { font: 6.5px/9px var(--body), serif; color: var(--ink); white-space: nowrap; overflow: hidden; }
  .item.short { height: 17px; }
</style>
</head>
<body>
<div class="canvas">

  <section class="sheet cover">
    <div class="sheet-frame"></div>
    <div class="season">SUMMER/AUTUMN MENU 2013</div>
    <div class="wordmark">VELLANO</div>
    <div class="tagline">LOCAL FRESH MODERN</div>
    <div class="rule" style="top:638px"></div>
    <div class="web">www.vellanorestaurant.com</div>
    <div class="rule" style="top:696px"></div>
    <div class="address">Vellano*, 14 Harbor View Lane,<br>Rockland, ME. 04800</div>
    <div class="dots" style="top:814px"></div>
    <div class="sourcing">All meat, fish and vegetables are locally sourced</div>
    <div class="dots" style="top:870px"></div>
    <div class="daily">Please ask for the daily specials<br>restaurant served daily</div>
  </section>

  <section class="sheet back">
    <div class="sheet-frame"></div>
    <div class="wordmark">VELLANO</div>
    <div class="motto">Local. Fresh. Modern.</div>
    <div class="heading" style="top:366px">Opening hours</div>
    <div class="hours">
      <div>Monday to Friday<br>9am – 5pm</div>
      <div>Saturday<br>9am – 5pm</div>
      <div>Sunday<br>10am – 4pm</div>
    </div>
    <div class="heading" style="top:462px">Contact us</div>
    <div class="contact">Vellano Restaurant<br>Rockland<br>14 Harbor View Lane<br>ME. 04800</div>
    <div class="phone">Telephone: 207.555.0143</div>
  </section>

  <section class="sheet menu">
    <div class="menu-band"><span style="left:124px">Vellano Menu</span><span style="left:434px">Restaurant Menu</span></div>

    <div class="section" style="left:24px; top:108px">
      <h2>Coffee &amp; Tea's ...</h2>
      <div class="item"><div class="item-head"><span>Cappuccino</span><span class="price">$1.95</span></div><p>A shot of espresso and frothed milk dusted with chocolate powder</p></div>
      <div class="item"><div class="item-head"><span>Latte (white coffee)</span><span class="price">$1.95</span></div><p>A shot of espresso topped up with hot milk</p></div>
      <div class="item"><div class="item-head"><span>Americano (black coffee)</span><span class="price">$1.75</span></div><p>A shot of espresso topped up with hot water</p></div>
      <div class="item"><div class="item-head"><span>Chocolate</span><span class="price">$1.85</span></div><p>Smooth and rich hot chocolate with a milk froth</p></div>
      <div class="item"><div class="item-head"><span>Espresso</span><span class="price">$1.20</span></div><p>A short rich shot of gourmet coffee</p></div>
      <div class="item"><div class="item-head"><span>Decaffeinated Coffee</span><span class="price">$1.60</span></div><p>A cup of decaffeinated coffee served with hot milk</p></div>
      <div class="item"><div class="item-head"><span>Vanilla Late</span><span class="price">$1.90</span></div><p>A shot of espresso topped up with hot milk with a hint of vanilla</p></div>
      <div class="item"><div class="item-head"><span>Tea</span><span class="price">$1.55</span></div><p>A pot of English tea</p></div>
      <div class="item"><div class="item-head"><span>Green Tea</span><span class="price">$1.65</span></div><p>An individual cup of green tea</p></div>
    </div>

    <div class="section" style="left:310px; top:108px">
      <h2>Baguettes &amp; Sandwiches ...</h2>
      <div class="item"><div class="item-head"><span>Tuna Mayo</span><span class="price">$2.95</span></div><p>Tuna &amp; Mayonnaise with sweet corn in either a baguette or sandwich</p></div>
      <div class="item"><div class="item-head"><span>BLT</span><span class="price">$2.95</span></div><p>Bacon, Lettuce and Tomato with salad in either a baguette or sandwich</p></div>
      <div class="item"><div class="item-head"><span>The Big Breakfast</span><span class="price">$2.70</span></div><p>Everything you need to start the day! Sausage, scrambled egg, bacon and mushrooms</p></div>
      <div class="item"><div class="item-head"><span>Coronation Chicken</span><span class="price">$2.85</span></div><p>Simple creamy coronation chicken in either a baguette or sandwich</p></div>
      <div class="item"><div class="item-head"><span>Chilli Chicken</span><span class="price">$2.90</span></div><p>Mild spicy pieces of chicken with mayo in either a baguette or sandwich</p></div>
      <div class="item"><div class="item-head"><span>Peri Peri Chicken</span><span class="price">$2.60</span></div><p>Same like it HOT with our peri chicken, you choose the spice, Mild, Medium or Hot</p></div>
      <div class="item"><div class="item-head"><span>Bacon</span><span class="price">$2.55</span></div><p>with a choice of Smoked or Un-Smoked bacon</p></div>
      <div class="item"><div class="item-head"><span>Brie, Salad &amp; Cranberry Or Mango Chutney (veggie)</span><span class="price">$2.75</span></div><p>A meat free sensation</p></div>
      <div class="item short"><div class="item-head"><span>Vegetable Nugget With Sweet Thai Chilli (veggie)</span><span class="price">$2.65</span></div></div>
    </div>

    <div class="section" style="left:24px; top:246px; top:246px"></div>

    <div class="section" style="left:24px; top:245px; top:245px"></div>

    <div class="section" style="left:24px; top:246px; display:none"></div>

    <div class="section" style="left:24px; top:247px; display:none"></div>

    <div class="section" style="left:24px; top:248px; display:none"></div>

    <div class="section" style="left:24px; top:246px; display:none"></div>

    <div class="section" style="left:24px; top:246px; display:none"></div>

    <div class="section" style="left:24px; top:384px">
      <h2>Cold Drinks</h2>
      <div class="item"><div class="item-head"><span>Orange Juice</span><span class="price">$1.50</span></div><p>Made with fresh oranges</p></div>
      <div class="item"><div class="item-head"><span>Apple Juice</span><span class="price">$1.50</span></div><p>Made with the finest apples</p></div>
      <div class="item"><div class="item-head"><span>Sparkling Water</span><span class="price">$1.50</span></div><p>Carbonated spring water in a choice of flavours</p></div>
      <div class="item"><div class="item-head"><span>Spring Water</span><span class="price">$1.50</span></div><p>Natural mineral water</p></div>
      <div class="item"><div class="item-head"><span>Cranberry Juice</span><span class="price">$1.50</span></div><p>Home made fresh cranberry juice</p></div>
      <div class="item"><div class="item-head"><span>Dandelion and Burdock</span><span class="price">$1.75</span></div><p>Fermented botanical full strength infusions of dandelion and burdock with ginger extract</p></div>
      <div class="item"><div class="item-head"><span>Home Made Lemonade</span><span class="price">$1.99</span></div><p>Fermented botanical lemon drink with ginger and herbal extracts</p></div>
      <div class="item"><div class="item-head"><span>Elderflower Lemonade</span><span class="price">$1.99</span></div><p>Made from fresh elderflowers</p></div>
    </div>

    <div class="section" style="left:310px; top:384px">
      <h2>Desserts &amp; Cakes</h2>
      <p class="intro">Why not indulge yourself with our selection of home made cakes and pastries, the perfect complement to go with a lovely coffee.</p>
      <div class="item"><div class="item-head"><span>A Slice of Cake</span><span class="price">$2.30</span></div><p>Served with cream</p></div>
      <div class="item"><div class="item-head"><span>Handmade Scone</span><span class="price">$1.35</span></div><p>Served with butter</p></div>
      <div class="item"><div class="item-head"><span>Handmade Jam Scone</span><span class="price">$1.80</span></div><p>Served with cream</p></div>
      <div class="item short"><div class="item-head"><span>Muffins</span><span class="price">$1.35</span></div></div>
      <div class="item short"><div class="item-head"><span>Danish Pastries</span><span class="price">$1.20</span></div></div>
      <div class="item short"><div class="item-head"><span>Cookies</span><span class="price">$1.00</span></div></div>
      <div class="item short"><div class="item-head"><span>Flap Jacks</span><span class="price">$1.35</span></div></div>
      <div class="item short"><div class="item-head"><span>Carrot Cake</span><span class="price">$1.00</span></div></div>
    </div>
  </section>

</div>
</body>
</html>
```